Professional Baby Bottle Bank Print Design

We need a baby bottle design that is 4.25" wide x 2.28" tall with a maximum of 6 colors (white is counted as a color).

The bottle design needs to be fun but professional. Bottles with cartoon images on it will be rejected immediately.

The bottle design wraps around the bottle. See examples here: https://wendrix.net/cat/BabyBottles/OrvelJarsKit/5

Minimum font size is 10pt.

The bottle design must have the following text on it:
Main Text: Love them both
Paragraph text: Our ministry’s aim is to not only save unborn babies, but to provide love, support, and life-saving resources for vulnerable women in our community. By filling this bottle with cash, checks, and spare coins and returning it on collection day, you are truly saving and changing lives!
Optional text: Thank you!

We are including an example file and a template file. You do NOT have to use the template - but your file has to be the exact size mentioned. If you don't design as well as our sample, please don't waste our time by spamming us with hundreds of designs. We will ban design houses that spam us with designs that are more layouts (and not well designed).

Please note - white is a color. You don't have to do a box - but anything you don't make white will be see-through.

We will take the winners of this contest to a survey with the customers. We may choose two and edit the text of one slightly to be different. We must know the fonts used.

No gradients unless they are half-toned with relatively big sized dots.

Target Market(s)

Church Attendees coming from a Pregnancy Center

Industry/Entity Type

Religious Christian Churches

Requirements
Must have
• Professional, great palette, wording as described.
Nice to have
• Integrated design across the whole space with areas for text (no text all the way across)
Should not have
• Cartoon figures; elements shoved together that don't go together (i.e. - actually design something)

```html
<!DOCTYPE html>
<html lang="en">
<head>
<meta charset="utf-8">
<title>Love Them Both – Baby Bottle Wrap</title>
<link rel="stylesheet" href="https://fonts.googleapis.com/css2?family=Courgette&family=Josefin+Sans:wght@300;400&family=Allura&display=swap">
<style>
  :root {
    --page: #ffffff;
    --coral: #f59b7c;
    --coral-deep: #f4845f;
    --blush: #f8b49c;
    --sun: #f3d55b;
    --navy: #404e86;
    --ink-light: #ffffff;
  }
  html, body {
    margin: 0;
    padding: 0;
    width: 1200px;
    height: 1200px;
    overflow: hidden;
    background: var(--page);
  }
  .bottle-wrap {
    position: absolute;
    left: 175px;
    top: 372px;
    width: 850px;
    height: 456px;
    overflow: hidden;
    background: var(--coral);
  }
  .wrap-art {
    position: absolute;
    inset: 0;
    width: 850px;
    height: 456px;
  }
  .mission-text {
    position: absolute;
    left: 36px;
    top: 56px;
    margin: 0;
    font-family: "Courgette", cursive;
    font-size: 14px;
    line-height: 26.7px;
    color: var(--ink-light);
    white-space: nowrap;
  }
  .thank-you {
    position: absolute;
    left: 130px;
    top: 372px;
    margin: 0;
    font-family: "Courgette", cursive;
    font-size: 14px;
    color: var(--ink-light);
  }
  .title-love { font-family: "Josefin Sans", sans-serif; font-weight: 300; fill: var(--sun); }
  .title-them { font-family: "Allura", cursive; fill: var(--ink-light); }
  .title-both { font-family: "Josefin Sans", sans-serif; font-weight: 400; fill: var(--navy); }
</style>
</head>
<body>
  <div class="bottle-wrap">
    <svg class="wrap-art" viewBox="0 0 850 456" xmlns="http://www.w3.org/2000/svg">
      <defs>
        <radialGradient id="motherBabyTones" cx="0.55" cy="0.5" r="0.6">
          <stop offset="0" stop-color="#fbe3d8"/>
          <stop offset="0.45" stop-color="#f3c0a4"/>
          <stop offset="0.8" stop-color="#8a6f98"/>
          <stop offset="1" stop-color="#404e86"/>
        </radialGradient>
      </defs>
      <circle class="accent-circle" cx="37" cy="35" r="39" fill="var(--coral-deep)"/>
      <circle class="accent-circle" cx="101" cy="0" r="37" fill="var(--sun)"/>
      <circle class="accent-circle" cx="866" cy="305" r="38" fill="var(--blush)"/>
      <rect class="illustration-area" x="228" y="0" width="336" height="456" rx="40"
            fill="url(#motherBabyTones)" role="img"
            aria-label="Illustration of a mother with long dark hair cradling her sleeping newborn, among soft leaves and sun circles"/>
      <text class="title-love" x="578" y="165" font-size="235" textLength="254" lengthAdjust="spacingAndGlyphs">Love</text>
      <text class="title-them" x="580" y="278" font-size="120" textLength="255" lengthAdjust="spacingAndGlyphs">them</text>
      <text class="title-both" x="584" y="405" font-size="140" textLength="244" lengthAdjust="spacingAndGlyphs">Both</text>
    </svg>
    <p class="mission-text">Our ministry’s aim is to<br>not only save unborn<br>babies, but to provide love,<br>support, and life-saving<br>resources for vulnerable<br>women in our community.<br>By filling this bottle with<br>cash, checks, and spare<br>coins and returning it on<br>collection day, you are<br>truly saving and changing<br>lives!</p>
    <p class="thank-you">Thank you</p>
  </div>
</body>
</html>
```